Luxury Brand Real Estate For Sale sign

**Update** I've added some examples from the internet of other signs that have a look similar to what I would like to see. I do not want my personal name in the sign. And the word FOR SALE Does not need to be so large - it can be more subtle.
I want to create a Real Estate for sale sign for my company that will be used for luxury/higher end real estate listings. I’m sharing my business card as well as a logo with new teal color to show what we're moving towards: we’re using Teal, white, black and gold.
Hoping the sign is simple, sophisticated and eye catching.
The sign should be 24" wide by 30" tall including the company name: Harbor Crest Realty Group and our logo, office phone number 727-555-0148 and website www.hcrgproperty.example the words "For Sale"
Optional to add this e-mail address info@hcrgproperty.example to the sign
Luxury home buyers
Real Estate

```html
<!DOCTYPE html>
<html lang="en">
<head>
<meta charset="utf-8">
<title>Harbor Crest Realty Group — For Sale Sign</title>
<link rel="stylesheet" href="https://fonts.googleapis.com/css2?family=Bebas+Neue&family=Josefin+Sans:wght@400&family=Oswald:wght@600&display=swap">
<style>
  :root {
    --teal: #0a8480;
    --charcoal: #474747;
    --white: #ffffff;
    --wash-light: #f4fafd;
    --wash-blue: #d6ecf8;
    --stage: #e9ecef;
  }
  * { margin: 0; padding: 0; box-sizing: border-box; }
  html, body {
    width: 1200px; height: 1200px; overflow: hidden;
    background: var(--stage);
  }
  .sign {
    position: absolute; left: 160px; top: 50px;
    width: 880px; height: 1100px;
    background:
      radial-gradient(ellipse at 80% 8%, var(--wash-blue) 0%, transparent 45%),
      radial-gradient(ellipse at 10% 85%, #e3f2fa 0%, transparent 40%),
      linear-gradient(180deg, #e2f1fa 0%, var(--wash-light) 45%, #eaf5fb 100%);
    box-shadow: 0 10px 30px rgba(0,0,0,0.12);
  }
  .brand {
    position: absolute; left: 106px; top: 135px;
    display: flex; align-items: center; height: 196px;
  }
  .brand-mark {
    width: 96px; height: 96px;
    border: 4px solid var(--teal);
  }
  .brand-divider {
    width: 3px; height: 196px; background: var(--charcoal);
    margin: 0 34px 0 124px;
  }
  .brand-name {
    font-family: "Josefin Sans", sans-serif; font-weight: 400;
    color: var(--teal); font-size: 32px; line-height: 1.25;
    letter-spacing: 2px; text-transform: uppercase;
  }
  .offer {
    position: absolute; left: 96px; top: 412px; width: 700px;
  }
  .offer-title {
    height: 262px; background: var(--white);
    border: 4px solid var(--teal); border-bottom: none;
    display: flex; align-items: center; justify-content: center;
    font-family: "Bebas Neue", sans-serif; font-size: 240px; line-height: 1;
    padding-top: 22px; letter-spacing: 2px;
  }
  .offer-title .for { color: var(--charcoal); margin-right: 34px; }
  .offer-title .sale { color: var(--teal); }
  .offer-phone {
    height: 218px; background: var(--teal);
    display: flex; align-items: center; justify-content: center;
    font-family: "Oswald", sans-serif; font-weight: 600;
    font-size: 128px; color: var(--white); letter-spacing: -1px;
  }
  .website {
    position: absolute; left: 0; right: 0; top: 985px;
    text-align: center;
    font-family: "Oswald", sans-serif; font-weight: 600;
    font-size: 40px; letter-spacing: 7px; color: var(--charcoal);
    text-transform: uppercase;
  }
</style>
</head>
<body>
  <main class="sign">
    <header class="brand">
      <div class="brand-mark" aria-hidden="true"></div>
      <div class="brand-divider" aria-hidden="true"></div>
      <div class="brand-name">Harbor Crest<br>Realty Group</div>
    </header>
    <section class="offer">
      <div class="offer-title"><span class="for">For</span><span class="sale">Sale</span></div>
      <div class="offer-phone">727-555-0148</div>
    </section>
    <p class="website">www.hcrgproperty.example</p>
  </main>
</body>
</html>
```